small business website design

***Update: need the design to be coded into a wordpress or similar format***
Need a website for a small business with big plans. No online ordering etc but business description and contact details pages, a page showing products we use and page for customers or suppliers to register with us. Also want links to chirpnest. We have a logo existing but also open to any improvements on the design. We have an existing website we created and looks very DIY but you can get some info from it to help create your design for us.
Hi Everyone, we didn't make it clear at the beginning but we would like the final design to be in a coded format and ready to upload to a URL. I have to apologise and admit to my lack of knowledge of the design process.
Oil / gas and industrial plant managers.
Small Business

```html
<!DOCTYPE html>
<html lang="en">
<head>
<meta charset="utf-8">
<title>Keelway – Plus For Your Business</title>
<link href="https://fonts.googleapis.com/css2?family=Open+Sans:wght@300;400;600;700&display=swap" rel="stylesheet">
<style>
  :root {
    --accent: #2b8fcf;
    --nav-text: #ffffff;
    --hero-top: #6f6152;
    --hero-mid: #4a362c;
    --hero-low: #7a6a5c;
    --dark: #0d0e10;
    --service-title: #e6e6d6;
    --logo-bg: #c9d3dd;
    --logo-ink: #1f6f7a;
    --logo-sub: #23384a;
    --white: #ffffff;
  }
  * { margin: 0; padding: 0; box-sizing: border-box; }
  html, body { width: 1200px; height: 743px; overflow: hidden; background: var(--dark); }
  body { font-family: "Open Sans", sans-serif; position: relative; }

  .hero {
    position: absolute; left: 0; top: 0; width: 1200px; height: 547px;
    background:
      linear-gradient(rgba(20,14,10,0.35), rgba(20,14,10,0.35)),
      linear-gradient(115deg, var(--hero-top) 0%, var(--hero-mid) 35%, #5a4234 60%, var(--hero-low) 85%, #9a9288 100%);
  }

  .brand {
    position: absolute; left: 51px; top: 0; width: 247px; height: 63px;
    background: var(--logo-bg);
    display: flex; flex-direction: column; align-items: center; justify-content: center;
  }
  .brand-name { font-size: 30px; font-weight: 700; color: var(--logo-ink); line-height: 1; letter-spacing: 1px; }
  .brand-tagline { font-size: 10px; font-weight: 400; color: var(--logo-sub); margin-top: 4px; }

  .main-nav { position: absolute; top: 0; left: 425px; display: flex; height: 44px; }
  .main-nav a {
    color: var(--nav-text); text-decoration: none; text-transform: uppercase;
    font-size: 13.5px; font-weight: 400; letter-spacing: 0.3px;
    height: 44px; line-height: 38px; padding: 0 21px;
  }
  .main-nav a.is-active { background: var(--accent); border-radius: 0 0 3px 3px; padding: 0 20px; }

  .hero-title {
    position: absolute; top: 190px; left: 0; width: 1128px; text-align: center;
    font-size: 36px; font-weight: 300; color: var(--white); letter-spacing: -0.3px;
  }
  .hero-lead {
    position: absolute; top: 262px; left: 0; width: 1128px; text-align: center;
    font-size: 18.5px; font-weight: 300; color: #f1ece6;
  }
  .hero-button {
    position: absolute; left: 483px; top: 354px; width: 160px; height: 61px;
    background: var(--accent); color: var(--white); border-radius: 3px;
    font-size: 18.5px; font-weight: 300; text-align: center; line-height: 61px; text-decoration: none;
  }

  .services { position: absolute; left: 0; top: 547px; width: 1200px; height: 196px; background: var(--dark); }
  .service { position: absolute; top: 75px; text-align: center; width: 320px; }
  .service-title { font-size: 25px; font-weight: 300; color: var(--service-title); letter-spacing: -0.5px; }
  .service-icon {
    position: absolute; top: 59px; border: 2px solid var(--white); border-radius: 3px;
    display: flex; align-items: center; justify-content: center; height: 70px;
  }
  .service--media { left: 17px; }
  .service--retail { left: 403px; }
  .service--finance { left: 789px; }
</style>
</head>
<body>
  <header class="hero" role="img" aria-label="Photo looking up at the rust-red steel lattice of a large bridge tower beside a pale stone pylon">
  </header>

  <div class="brand">
    <span class="brand-name">Keelway</span>
    <span class="brand-tagline">Plus For Your Business</span>
  </div>

  <nav class="main-nav">
    <a class="is-active" href="#">Homepage</a>
    <a href="#">About Us</a>
    <a href="#">Vision</a>
    <a href="#">Expertise</a>
    <a href="#">Services</a>
    <a href="#">Contact Us</a>
  </nav>

  <h1 class="hero-title">PLUS YOUR BUSINESS BY KEELWAY</h1>
  <p class="hero-lead">A total facilities management solutions consultancy - linking businessess across the market.</p>
  <a class="hero-button" href="#">Read More</a>

  <section class="services">
    <div class="service service--media">
      <h2 class="service-title">Media Marketting</h2>
      <div class="service-icon" style="left:129px;width:61px;">
        <svg width="40" height="40" viewBox="0 0 40 40" aria-hidden="true">
          <g fill="#fff" transform="translate(20 20)">
            <rect x="-4" y="-18" width="8" height="36" rx="1"/>
            <rect x="-4" y="-18" width="8" height="36" rx="1" transform="rotate(45)"/>
            <rect x="-4" y="-18" width="8" height="36" rx="1" transform="rotate(90)"/>
            <rect x="-4" y="-18" width="8" height="36" rx="1" transform="rotate(135)"/>
            <circle r="13"/>
          </g>
          <circle cx="20" cy="20" r="5.5" fill="#0d0e10"/>
        </svg>
      </div>
    </div>

    <div class="service service--retail">
      <h2 class="service-title">Retail Management</h2>
      <div class="service-icon" style="left:123px;width:73px;">
        <svg width="44" height="40" viewBox="0 0 44 40" aria-hidden="true">
          <path d="M11 4 H33 L42 36 H2 Z" fill="#fff"/>
          <rect x="20" y="8" width="4" height="7" fill="#0d0e10"/>
          <rect x="19.5" y="19" width="5" height="8" fill="#0d0e10"/>
          <rect x="19" y="30" width="6" height="6" fill="#0d0e10"/>
        </svg>
      </div>
    </div>

    <div class="service service--finance">
      <h2 class="service-title">Financial Management</h2>
      <div class="service-icon" style="left:128px;width:62px;">
        <svg width="36" height="36" viewBox="0 0 36 36" aria-hidden="true">
          <rect x="3" y="3" width="30" height="30" rx="3" fill="#fff"/>
        </svg>
      </div>
    </div>
  </section>
</body>
</html>
```